Design Project (Main Brochure)

We are a manually therapy based physical therapy clinic. We already have a brochure and we like the material on it. We would just like a new design We want this to be a very professional looking brochure. Something that will catch a persons eye and make them impressed with our clinic before they even read it. We also want it to have a modern style to it but not over done because we do still have a high number of elderly patients.

Industry/Entity Type

Physical Therapy

Requirements
Must have
• We are hoping to find a good color scheme to match our logo.
Nice to have
• We want this to look professionally done and to show obvious improvements from our previous brochure.

```html
<!DOCTYPE html>
<html lang="en">
<head>
<meta charset="utf-8">
<title>Calloway Physical Therapy – Brochure</title>
<link href="https://fonts.googleapis.com/css2?family=Didact+Gothic&family=Varela+Round&display=swap" rel="stylesheet">
<style>
  :root{
    --blue-deep:#1b5fd9;
    --blue-mid:#2e8ff0;
    --blue-bright:#3aa8f5;
    --blue-cyan:#5fd0fb;
    --blue-pale:#d6ecfb;
    --blue-mist:#eef7fd;
    --ink:#1a1a1a;
    --accent:#2f8de8;
    --white:#ffffff;
  }
  *{box-sizing:border-box;margin:0;padding:0}
  html,body{width:1200px;height:931px;overflow:hidden;background:#f2f4f7}
  .brochure{position:relative;width:1200px;height:931px;background:var(--white);overflow:hidden;
    font-family:"Didact Gothic",sans-serif;color:var(--ink)}
  .backdrop{position:absolute;inset:0}
  .panel-title{position:absolute;height:72px;border-radius:36px;
    background:linear-gradient(90deg,var(--blue-deep),var(--blue-mid) 55%,var(--blue-cyan));
    color:var(--white);font-family:"Varela Round",sans-serif;font-size:20px;line-height:1.25;
    display:flex;align-items:center;justify-content:center;text-align:center;
    box-shadow:0 0 0 6px rgba(255,255,255,.85),0 0 0 8px rgba(90,170,240,.5)}
  .column{position:absolute;font-size:14.5px;line-height:1.4}
  .column p{position:relative;padding-left:12px;margin-bottom:20px}
  .column p::before{content:"";position:absolute;left:0;top:8px;width:5px;height:5px;border-radius:50%;background:var(--accent)}
  .hl{color:var(--accent)}
  .column .divided{padding-bottom:18px;border-bottom:1px solid var(--blue-mid);margin-bottom:18px}
  .photo{position:absolute;border-radius:50%;border:10px solid var(--blue-mid);
    box-shadow:0 0 0 10px rgba(255,255,255,.9),0 0 0 16px rgba(120,190,245,.45)}
  .photo--therapist{left:-40px;top:600px;width:420px;height:420px;
    background:radial-gradient(circle at 55% 45%,#b8a48e,#5e6a72 60%,#3a4650)}
  .photo--neck{left:455px;top:650px;width:300px;height:300px;
    background:radial-gradient(circle at 45% 50%,#d3a98a,#8a6a5a 55%,#3b3b3d)}
  .photo--arm{left:905px;top:-40px;width:300px;height:300px;
    background:radial-gradient(circle at 50% 55%,#d9b39a,#a4a8a6 60%,#7a7f82)}
</style>
</head>
<body>
<main class="brochure">
  <svg class="backdrop" width="1200" height="931" viewBox="0 0 1200 931" aria-hidden="true">
    <defs>
      <linearGradient id="topBand" x1="0" y1="0" x2="1" y2="1">
        <stop offset="0" stop-color="#6cc3f7"/>
        <stop offset=".6" stop-color="#2e8ff0"/>
        <stop offset="1" stop-color="#1b5fd9"/>
      </linearGradient>
      <linearGradient id="lowWash" x1="0" y1="0" x2="0" y2="1">
        <stop offset="0" stop-color="#eef7fd"/>
        <stop offset="1" stop-color="#bfe0f8"/>
      </linearGradient>
    </defs>
    <path d="M0 0H1200V300C1050 230 900 160 700 150C480 140 300 220 0 200Z" fill="url(#topBand)"/>
    <path d="M0 180C300 205 480 125 700 135C900 145 1050 215 1200 285V300C1050 230 900 160 700 150C480 140 300 220 0 200Z" fill="#ffffff" opacity=".85"/>
    <path d="M0 210C300 230 500 160 720 170C920 180 1060 250 1200 320V340C1060 270 920 200 720 190C500 180 300 250 0 230Z" fill="#9fd4f8" opacity=".6"/>
    <path d="M0 931V650C250 700 500 760 800 700C980 665 1100 620 1200 600V931Z" fill="url(#lowWash)"/>
    <path d="M400 931C600 860 850 790 1200 740V931Z" fill="#d6ecfb" opacity=".8"/>
  </svg>

  <div class="photo photo--therapist" role="img" aria-label="Photo: therapist treating a patient's neck on a treatment table"></div>
  <div class="photo photo--neck" role="img" aria-label="Photo: close-up of a therapist working on a patient's neck"></div>
  <div class="photo photo--arm" role="img" aria-label="Photo: hands-on treatment of a patient's arm"></div>

  <h2 class="panel-title" style="left:30px;top:105px;width:340px">Why choose Calloway<br>Phsical Therapy?</h2>
  <h2 class="panel-title" style="left:440px;top:95px;width:320px">Why Try Physical<br>Therapy First?</h2>
  <h2 class="panel-title" style="left:845px;top:270px;width:320px">What to Expect your<br>First Visit</h2>

  <section class="column" style="left:30px;top:205px;width:345px">
    <p>Our team of physical therapists are <span class="hl">unmatched in Riverton</span> for their combination of post-graduate manual skills.</p>
    <p>Our patients get <span class="hl">results fast</span> with our care. All patients are treated one-on-one by a licensed physical therapist.</p>
    <p>We utilize a <span class="hl">manual therapy approach</span> to restore your movement and function. Our therapists work hands-on to correct problems in joints, muscle tissues, or connective tissues.</p>
    <p>We strive to <span class="hl">educate our patients</span> in all facets of health. We believe that a patient who thoroughly understands his or her condition will have a more successful outcome.</p>
  </section>

  <section class="column" style="left:440px;top:190px;width:330px">
    <p class="divided"><span class="hl">The Best Choice:</span> PT is the best choice for the least invasive, fastest treatment approach to decrease pain and increase function. PT has many different tools to quickly decrease symptoms AND resolve dysfunctions permanently--returning you to your pain--free life!</p>
    <p class="divided"><span class="hl">The Early Choice:</span> Early intervention is often the key to successful treatment. Don't--wait early physical therapy works fastest!</p>
    <p class="divided"><span class="hl">The Right Choice:</span> Physical Therapy is the right choice because it treats the problem rather than just the symptoms.</p>
    <p><span class="hl">Your First Visit:</span> You will receive a full evaluation by your PT. This comprehensive visit will likely take 45-60 minutes and will identify your impairment (pain, muscle weakness, muscle tightness, deconditioning) that is affecting your overall function.</p>
  </section>

  <section class="column" style="left:850px;top:365px;width:325px">
    <p><span class="hl">Bring Referral:</span> and also your insurance card.</p>
    <p><span class="hl">Paperwork:</span> There are a few forms to be filled out. You can visit our website callowaypt.com to print and fill out these forms and bring to your appointment. You can also fax or email paperwork to our office.</p>
    <p><span class="hl">Initial Evaluation:</span> You will discuss with your Physical Therapist your medical history and standing, or lying down.</p>
    <p><span class="hl">Examination:</span> You should wear something that you are comfortable moving around in whether sitting, standing, or lying down.</p>
    <p><span class="hl">Begin Treatment</span></p>
    <p><span class="hl">Discuss Treatment Plan</span></p>
    <p><span class="hl">Schedule Visits:</span> Bring your calendar so that we are able to set up all your appointments at that time.</p>
    <p>Your copay will be collected at the end of your visit. We accept cash, check or credit card as well as offer Care Finance Plan.</p>
  </section>
</main>
</body>
</html>
```